依頼詳細
ホテル内レストランなので、高級感ラグジュアリー感のあるデザイン希望

ターゲット:ホテルご宿泊者様向け

・ディナーご利用時1ドリンクサービス
・カラオケ個室完備
・パーティー
記載項目
社名:株式会社ミルトフォレスト
店舗名:KAEDE NOGIZAKAA
住所: 〒107-0061 東京都港区北青山5-27-9アパホテル&リゾート〈六本木駅東〉1階
TEL/FAX 03-6781-2294
サイズ
A6
ページ数
片面
希望イメージ
シンプル 複雑
単色 カラフル
暗い 明るい
日常 高級
遊び心 厳粛
未来的 伝統的
女性的 男性的
希望する色
設定なし
納品ファイル
• 高解像度JPG (.jpg)
• イラストレーター形式 (.ai)
• PNG形式 (.png)
補足説明
本コンペ入選者でランチ半額のチラシを依頼したく思っております。よろしくお願いします。
記載いただきたい内容の文言追記します。
写真も店内写真とビュッフェ写真を追加します。よろしくお願いいたします。

・パーティー
→3,000円/ブッフェ+free drink

→5,000円/ブッフェ+freedrink

→1万円/ブッフェ+freedrink

※貸切
・30名以上/15万円以上/2時間
追加料金→30分..1万円/1時間..2万円

・カラオケ→1時間..大7,000円/小5,000円

※予算・内容に応じてご予約承ります。
■ 選んだ理由

コンセプトのマッチと表現方法、今後展開したいイメージにあっているため、選ばせていただきました。チラシをぱっとみて、何を伝えたいのかが読み取りやすい構成が素晴らしいと感じました。

■ 提案者全員のお礼・コメント

今回たくさんの方にご提案いただき本当にありがとうございました。弊社複数の事業展開をしており、
新店もぞくぞくオープンしていくので、広告需要が高いです。今後ともみなさまからのご提案を何卒よろしくお願いいたします!

```html
<!DOCTYPE html>
<html lang="ja">
<head>
<meta charset="utf-8">
<title>KAEDE NOGIZAKAA パーティーのご案内</title>
<link href="https://fonts.googleapis.com/css2?family=Shippori+Mincho:wght@500;700&family=Noto+Serif+JP:wght@400;600&family=Cormorant+Garamond:wght@500;600&display=swap" rel="stylesheet">
<style>
  :root {
    --ink: #0d0b0a;
    --night: #17120f;
    --white: #ffffff;
    --cream: #f3ece0;
    --gold-light: #d9c08a;
    --gold: #b8975a;
    --gold-deep: #8a6c38;
    --wine: #5a1418;
    --photo-warm: #b59a80;
    --photo-light: #e8ddd0;
    --photo-dark: #4a3a30;
  }
  * { margin: 0; padding: 0; box-sizing: border-box; }
  html, body { width: 850px; height: 1200px; overflow: hidden; background: var(--ink); }
  .flyer {
    position: relative;
    width: 850px;
    height: 1200px;
    overflow: hidden;
    background: var(--night);
    font-family: "Noto Serif JP", serif;
    color: var(--white);
  }
  .hero-photo {
    position: absolute;
    left: 0; top: 0;
    width: 850px; height: 835px;
    background:
      radial-gradient(ellipse 260px 200px at 640px 300px, rgba(110, 20, 30, 0.55), transparent 70%),
      radial-gradient(ellipse 300px 220px at 420px 560px, rgba(240, 230, 215, 0.75), transparent 70%),
      radial-gradient(ellipse 260px 180px at 130px 600px, rgba(120, 60, 45, 0.6), transparent 70%),
      linear-gradient(160deg, var(--photo-light) 0%, var(--photo-warm) 45%, var(--photo-dark) 100%);
  }
  .hero-shade {
    position: absolute;
    left: 0; top: 0;
    width: 850px; height: 835px;
    background: linear-gradient(180deg, rgba(20, 14, 10, 0.35) 0%, rgba(20, 14, 10, 0) 40%, rgba(20, 14, 10, 0.25) 100%);
  }
  .headline {
    position: absolute;
    left: 50px; top: 62px;
    font-family: "Shippori Mincho", serif;
    font-weight: 700;
    font-size: 50px;
    line-height: 1.36;
    letter-spacing: 0.06em;
    text-shadow: 0 2px 10px rgba(0, 0, 0, 0.45);
  }
  .offer {
    position: absolute;
    top: 680px;
    height: 125px;
    display: flex;
    align-items: center;
    justify-content: center;
    text-align: center;
    font-family: "Shippori Mincho", serif;
    font-weight: 700;
    font-size: 31px;
    line-height: 1.4;
    color: var(--white);
    background: linear-gradient(135deg, var(--gold-light) 0%, var(--gold) 50%, var(--gold-deep) 100%);
    opacity: 0.94;
    border: 2px solid rgba(255, 255, 255, 0.55);
    outline: 2px solid var(--gold);
    outline-offset: 5px;
    text-shadow: 0 1px 4px rgba(60, 40, 10, 0.5);
  }
  .offer--drink { left: 55px; width: 345px; }
  .offer--karaoke { left: 450px; width: 330px; }
  .intro {
    position: absolute;
    left: 50px; top: 870px;
    width: 450px;
    font-size: 19.5px;
    line-height: 1.85;
    letter-spacing: 0.02em;
    color: var(--cream);
  }
  .bar-photo {
    position: absolute;
    left: 525px; top: 835px;
    width: 325px; height: 225px;
    background:
      radial-gradient(ellipse 90px 60px at 90px 120px, rgba(230, 190, 120, 0.55), transparent 70%),
      radial-gradient(ellipse 120px 80px at 240px 90px, rgba(200, 150, 90, 0.45), transparent 70%),
      linear-gradient(180deg, #3a2a1e 0%, #221813 60%, #120d0a 100%);
  }
  .footer {
    position: absolute;
    left: 0; top: 1060px;
    width: 850px; height: 140px;
    background: var(--ink);
  }
  .brand-mark {
    position: absolute;
    left: 0; top: 0;
    width: 170px; height: 140px;
    background: var(--wine);
    display: flex;
    flex-direction: column;
    align-items: center;
    justify-content: center;
    gap: 12px;
  }
  .brand-mark__dot {
    width: 34px; height: 34px;
    border-radius: 50%;
    background: var(--white);
  }
  .brand-mark__name {
    font-family: "Cormorant Garamond", serif;
    font-weight: 600;
    font-size: 24px;
    letter-spacing: 0.12em;
    color: var(--white);
  }
  .shop {
    position: absolute;
    left: 200px; top: 16px;
    width: 630px;
  }
  .shop__name {
    font-family: "Cormorant Garamond", serif;
    font-weight: 600;
    font-size: 27px;
    letter-spacing: 0.06em;
    line-height: 1.2;
  }
  .shop__address {
    margin-top: 6px;
    font-size: 15.5px;
    line-height: 1.4;
    color: var(--cream);
    white-space: nowrap;
  }
  .shop__tel {
    margin-top: 8px;
    font-family: "Cormorant Garamond", serif;
    font-weight: 600;
    font-size: 38px;
    letter-spacing: 0.03em;
    line-height: 1.1;
  }
</style>
</head>
<body>
<div class="flyer">
  <div class="hero-photo" role="img" aria-label="ワイングラスで乾杯する手元と、テーブルに並ぶ料理の写真"></div>
  <div class="hero-shade"></div>

  <h1 class="headline">結婚式の二次会<br>各種パーティー<br>交流会など</h1>

  <div class="offer offer--drink">ディナーご利用時<br>1ドリンクサービス</div>
  <div class="offer offer--karaoke">カラオケ個室完備</div>

  <p class="intro">イタリアン＆フレンチを楽しめるミュージックバー。<br>広々とした落ち着いた空間は、<br>様々なシーンでご利用になれます。</p>

  <div class="bar-photo" role="img" aria-label="ボトルとグラスが並ぶバーカウンターの写真"></div>

  <footer class="footer">
    <div class="brand-mark">
      <span class="brand-mark__dot"></span>
      <span class="brand-mark__name">KAEDE</span>
    </div>
    <div class="shop">
      <p class="shop__name">KAEDE NOGIZAKAA</p>
      <p class="shop__address">東京都港区北青山5-27-9ルミエスホテル&amp;スイート〈青山駅北〉1階</p>
      <p class="shop__tel">TEL/FAX.03-6781-2294</p>
    </div>
  </footer>
</div>
</body>
</html>
```